Bright Pelvic Health Business Card

Need a business card for a surgical practice called Bright Pelvic Health. We have recently selected a logo (attached). The business card will need to have two formats:
1) One with the logo/physician name/ contact info on the front and location information on the back.
2) One in "appointment reminder card" style with the logo/ contact info/ date/ time on the front and the location information on the back.

The front side should include the following information:
- Logo
- Ravi K. Desai, MD FACOG
- phone: 469-555-0182
- fax: 1-469-555-0147
- email: admin@brightpelvic.example
- website: www.brightpelvichealth.example

The back side should have the office locations listed:
4812 Quarry Bend Dr, Plano, TX 75093
3650 Wrenfield Rd, Plano, TX 75025
2245 Brambleton Ln, Irving, TX 75038
915 S Garnet Ave B314, Dallas, TX 75201
1836 Tillman Pkwy, Grand Prairie, TX 75051
6417 Dorrance Way Dr, San Antonio, TX 78240
5920 Kessler Rd, Pasadena, TX 77504

Target Market(s)

1. Other physicians who might refer patients
2. Female patients

Industry/Entity Type

Business

Font styles to use
Other font styles liked:
• Tahoma for lettering

Requirements
Must have
• As per the instructions
Should not have
• No other images needed -- please try to keep font consistent with logo design. Can use Tahoma as the font for lettering.

```html
<!DOCTYPE html>
<html lang="en">
<head>
<meta charset="utf-8">
<title>Bright Pelvic Health – Business Card, Front Side</title>
<link href="https://fonts.googleapis.com/css2?family=Arimo&family=Noto+Sans:wght@400;700&display=swap" rel="stylesheet">
<style>
  :root {
    --ink: #000000;
    --paper: #ffffff;
    --card-edge: #8a8a8a;
    --mist: #dce3e3;
    --maroon: #6e0000;
    --stripe-light: #f4e6e6;
  }
  * { margin: 0; padding: 0; box-sizing: border-box; }
  html, body {
    width: 1200px;
    height: 900px;
    overflow: hidden;
    background: var(--paper);
  }
  .sheet {
    position: relative;
    width: 1200px;
    height: 900px;
    border: 2px solid var(--ink);
    background: var(--paper);
  }
  .side-label {
    position: absolute;
    left: 71px;
    top: 108px;
    font-family: "Arimo", Arial, sans-serif;
    font-size: 62px;
    font-weight: 400;
    color: var(--ink);
    line-height: 1;
  }
  .card {
    position: absolute;
    left: 75px;
    top: 180px;
    width: 1051px;
    height: 600px;
    border: 1px solid var(--card-edge);
    background: linear-gradient(to bottom, var(--mist) 0%, #f3f5f5 28%, var(--paper) 45%, var(--paper) 100%);
    font-family: "Noto Sans", Tahoma, sans-serif;
    color: var(--ink);
  }
  .physician {
    position: absolute;
    right: 42px;
    top: 46px;
    text-align: right;
  }
  .physician-name {
    font-size: 38px;
    font-weight: 700;
    line-height: 1.1;
  }
  .physician-credentials {
    font-size: 28px;
    font-weight: 400;
    line-height: 1.5;
  }
  .brand {
    position: absolute;
    left: 0;
    right: 0;
    top: 262px;
    display: flex;
    align-items: center;
    justify-content: center;
    gap: 24px;
  }
  .brand-mark {
    width: 58px;
    height: 58px;
    background: var(--maroon);
  }
  .brand-name {
    font-size: 68px;
    font-weight: 700;
    color: var(--ink);
    line-height: 1.2;
    white-space: nowrap;
  }
  .divider {
    position: absolute;
    left: 0;
    right: 0;
    top: 428px;
    height: 23px;
    background: linear-gradient(to bottom, var(--maroon) 0%, #a55a5a 30%, var(--stripe-light) 50%, #a55a5a 70%, var(--maroon) 100%);
  }
  .contact {
    position: absolute;
    left: 0;
    right: 0;
    top: 465px;
    text-align: center;
    font-size: 26px;
    line-height: 36px;
    list-style: none;
  }
</style>
</head>
<body>
  <main class="sheet">
    <h1 class="side-label">Front Side</h1>
    <section class="card" aria-label="Business card front">
      <div class="physician">
        <p class="physician-name">Ravi K. Desai</p>
        <p class="physician-credentials">MD FACOG</p>
      </div>
      <div class="brand">
        <span class="brand-mark" aria-hidden="true"></span>
        <span class="brand-name">Bright Pelvic Health</span>
      </div>
      <div class="divider" aria-hidden="true"></div>
      <ul class="contact">
        <li>phone: 469-555-0182,&nbsp; fax: 1-469-555-0147</li>
        <li>email: admin@brightpelvic.example</li>
        <li>website: www.brightpelvichealth.example</li>
      </ul>
    </section>
  </main>
</body>
</html>
```